Business Design for Printed Shipping Tape

We need a company logo design to be printed on packaging natural color WAT tape for shipping boxes. www.brightmeadowkelp.com
The tape is 3" wide. Repeat pattern every 10 inches.
Would like our website vertical at one end side and "The Future of Nutrition" on the opposite end.

Industry/Entity Type

Health, Nutrition

Font styles to use
Sans Serif

Requirements
Must have
• Company Logo (attached) website and text "The Future of Nutrition"
Nice to have
• Tape is Natural Color.

```html
<!DOCTYPE html>
<html lang="en">
<head>
<meta charset="utf-8">
<title>Bright Meadow Kelp – Shipping Tape</title>
<link rel="stylesheet" href="https://fonts.googleapis.com/css2?family=Montserrat:wght@800&family=Jost:wght@400&family=Roboto+Condensed:wght@400&family=Great+Vibes&display=swap">
<style>
  :root {
    --backdrop-light: #e6e6e6;
    --backdrop-dark: #b9b9b9;
    --tape: #ffffff;
    --ink: #2b2b2b;
    --teal: #16876f;
  }
  * { margin: 0; padding: 0; box-sizing: border-box; }
  html, body { width: 984px; height: 1200px; overflow: hidden; }
  body {
    background: radial-gradient(ellipse at center, var(--backdrop-light) 0%, #d9d9d9 60%, var(--backdrop-dark) 100%);
    position: relative;
  }
  .tape-strip {
    position: absolute;
    left: 42px; top: 465px;
    width: 900px; height: 270px;
    background: var(--tape);
    box-shadow: 0 2px 8px rgba(0,0,0,.08);
  }
  .brand {
    position: absolute;
    left: 40px; top: 0; width: 300px; height: 100%;
    display: flex; align-items: center; justify-content: center; gap: 12px;
  }
  .brand-dot {
    width: 34px; height: 34px; border-radius: 50%;
    background: var(--teal); flex: none;
  }
  .brand-name {
    font-family: "Montserrat", sans-serif;
    font-weight: 800;
    font-size: 36px;
    line-height: 1.02;
    color: var(--ink);
    letter-spacing: -0.5px;
  }
  .website {
    position: absolute;
    top: 50%;
    font-family: "Roboto Condensed", sans-serif;
    font-size: 18px;
    color: var(--teal);
    white-space: nowrap;
    transform: translate(-50%, -50%) rotate(-90deg);
  }
  .website--left { left: 395px; }
  .website--right { left: 850px; }
  .slogan {
    position: absolute;
    left: 450px; top: 0; width: 370px; height: 100%;
    text-align: center;
    padding-top: 60px;
  }
  .slogan-lead {
    font-family: "Jost", sans-serif;
    font-size: 38px;
    color: var(--ink);
    line-height: 1;
    letter-spacing: -0.5px;
  }
  .slogan-script {
    font-family: "Great Vibes", cursive;
    font-size: 118px;
    color: var(--teal);
    line-height: 1;
    margin-top: -6px;
  }
</style>
</head>
<body>
  <section class="tape-strip" aria-label="Printed shipping tape repeat">
    <div class="brand">
      <span class="brand-dot"></span>
      <span class="brand-name">BRIGHT<br>MEADOW<br>KELP</span>
    </div>
    <p class="website website--left">www.brightmeadowkelp.com</p>
    <div class="slogan">
      <p class="slogan-lead">THE FUTURE OF</p>
      <p class="slogan-script">Nutrition</p>
    </div>
    <p class="website website--right">www.brightmeadowkelp.com</p>
  </section>
</body>
</html>
```